Need a design for Office wall, Pull up banner and brochure.

Hi there, We are looking for a design for our Mission, Vision and Values. We need it for our wall design, our pull up banner, and for our brochure. Full instructions have been provided in the Instructions png file submitted. Please let me know.

Our brand colours are:

Brand colours:
#0070BA
#000A3F
#6D6E71

Font styles to use
Other font styles liked:
• FF Meta Georgian Book

Colors

Designer to choose colors to be used in the design.

```html
<!DOCTYPE html>
<html lang="en">
<head>
<meta charset="utf-8">
<title>Brightmere Partners – Mission, Vision, Values</title>
<link rel="stylesheet" href="https://fonts.googleapis.com/css2?family=Open+Sans:wght@400;600;700&display=swap">
<style>
  :root {
    --brand-blue: #0070BA;
    --brand-navy: #000A3F;
    --brand-grey: #6D6E71;
    --swirl-lilac: #b3b6d6;
    --swirl-grey: #c0bfc6;
    --text-dark: #1e1e22;
    --bg-centre: #ffffff;
    --bg-edge: #dcdde0;
  }
  html, body {
    margin: 0;
    padding: 0;
    overflow: hidden;
  }
  body {
    width: 1200px;
    height: 848px;
    font-family: "Open Sans", Arial, sans-serif;
  }
  .canvas {
    position: relative;
    width: 1200px;
    height: 848px;
    background: radial-gradient(ellipse at 50% 50%, var(--bg-centre) 0%, #f3f3f4 45%, var(--bg-edge) 100%);
    overflow: hidden;
  }
  .brand-name {
    position: absolute;
    top: 104px;
    left: 912px;
    margin: 0;
    font-size: 22px;
    font-weight: 600;
    color: var(--brand-navy);
    line-height: 1;
  }
  .diagram {
    position: absolute;
    inset: 0;
  }
  .ring-label {
    font-family: "Open Sans", Arial, sans-serif;
    font-weight: 700;
    font-size: 33px;
    fill: #ffffff;
    letter-spacing: 1px;
  }
  .ring-copy {
    font-family: "Open Sans", Arial, sans-serif;
    font-size: 11.5px;
    fill: var(--text-dark);
  }
</style>
</head>
<body>
<main class="canvas">
  <p class="brand-name">Brightmere Partners</p>

  <svg class="diagram" width="1200" height="848" viewBox="0 0 1200 848" xmlns="http://www.w3.org/2000/svg">
    <defs>
      <linearGradient id="grey-ring" x1="0" y1="0" x2="0" y2="1">
        <stop offset="0" stop-color="#6a6b6e"/>
        <stop offset="1" stop-color="#3f4043"/>
      </linearGradient>
      <linearGradient id="blue-ring" x1="0" y1="0" x2="1" y2="1">
        <stop offset="0" stop-color="#1384cc"/>
        <stop offset="1" stop-color="#004f8a"/>
      </linearGradient>
      <linearGradient id="navy-ring" x1="0" y1="0" x2="1" y2="1">
        <stop offset="0" stop-color="#0a1450"/>
        <stop offset="1" stop-color="#000628"/>
      </linearGradient>
      <filter id="soft-shadow" x="-20%" y="-20%" width="140%" height="140%">
        <feDropShadow dx="0" dy="3" stdDeviation="4" flood-color="#000" flood-opacity="0.3"/>
      </filter>
      <clipPath id="cross-grey-blue"><circle cx="464" cy="387" r="34"/></clipPath>
      <clipPath id="cross-grey-navy"><circle cx="700" cy="390" r="34"/></clipPath>
      <clipPath id="cross-navy-blue"><circle cx="584" cy="620" r="38"/></clipPath>
      <path id="arc-mission" d="M 435 300 A 148 148 0 0 1 731 300"/>
      <path id="arc-vision" d="M 314 560 A 148 148 0 0 1 440 388"/>
      <path id="arc-values" d="M 730 390 A 148 148 0 0 1 856 565"/>
    </defs>

    <g class="swirls">
      <path d="M 425 205 A 210 210 0 0 1 720 150 A 270 270 0 0 0 425 205 Z" fill="var(--swirl-lilac)" opacity="0.75"/>
      <path d="M 590 105 A 230 230 0 0 1 765 330 A 300 300 0 0 0 590 105 Z" fill="var(--swirl-grey)" opacity="0.8"/>
      <path d="M 440 190 A 210 210 0 0 0 410 330 A 280 280 0 0 1 440 190 Z" fill="var(--swirl-grey)" opacity="0.75"/>
      <path d="M 270 640 A 210 210 0 0 1 385 385 A 280 280 0 0 0 270 640 Z" fill="var(--swirl-lilac)" opacity="0.75"/>
      <path d="M 305 640 A 215 215 0 0 0 470 745 A 280 280 0 0 1 305 640 Z" fill="var(--swirl-grey)" opacity="0.8"/>
      <path d="M 330 690 A 200 200 0 0 0 420 720 A 260 260 0 0 1 330 690 Z" fill="var(--swirl-lilac)" opacity="0.6"/>
      <path d="M 850 395 A 210 210 0 0 1 870 640 A 280 280 0 0 0 850 395 Z" fill="var(--swirl-lilac)" opacity="0.75"/>
      <path d="M 910 595 A 230 230 0 0 1 690 735 A 300 300 0 0 0 910 595 Z" fill="var(--swirl-grey)" opacity="0.8"/>
      <path d="M 630 700 A 210 210 0 0 0 800 700 A 280 280 0 0 1 630 700 Z" fill="var(--swirl-lilac)" opacity="0.6"/>
    </g>

    <g class="rings" fill="none" stroke-width="40" filter="url(#soft-shadow)">
      <circle class="ring-navy" cx="707" cy="538" r="147" stroke="url(#navy-ring)"/>
      <circle class="ring-grey" cx="583" cy="300" r="150" stroke="url(#grey-ring)"/>
      <circle class="ring-blue" cx="462" cy="535" r="147" stroke="url(#blue-ring)"/>
    </g>
    <g class="ring-crossings" fill="none" stroke-width="40">
      <circle cx="583" cy="300" r="150" stroke="url(#grey-ring)" clip-path="url(#cross-grey-blue)"/>
      <circle cx="583" cy="300" r="150" stroke="url(#grey-ring)" clip-path="url(#cross-grey-navy)"/>
      <circle cx="707" cy="538" r="147" stroke="url(#navy-ring)" clip-path="url(#cross-navy-blue)"/>
    </g>

    <text class="ring-label" dy="12"><textPath href="#arc-mission" startOffset="50%" text-anchor="middle">MISSION</textPath></text>
    <text class="ring-label" dy="12"><textPath href="#arc-vision" startOffset="50%" text-anchor="middle">VISION</textPath></text>
    <text class="ring-label" dy="12"><textPath href="#arc-values" startOffset="50%" text-anchor="middle">VALUES</textPath></text>

    <g class="icon-rocket" fill="var(--brand-blue)" transform="translate(556 226)">
      <path d="M 54 0 C 40 2 26 12 16 28 L 26 38 C 42 28 52 14 54 0 Z"/>
      <path d="M 14 24 L 4 24 L 0 32 L 10 32 Z"/>
      <path d="M 30 40 L 30 50 L 22 54 L 22 44 Z"/>
      <path d="M 12 36 L 18 42 L 6 54 L 2 52 Z"/>
    </g>

    <g class="icon-eye" transform="translate(419 461)">
      <path d="M 0 14 Q 22 -6 44 14 Q 22 34 0 14 Z" fill="var(--brand-navy)"/>
      <circle cx="22" cy="14" r="7" fill="#ffffff"/>
      <circle cx="22" cy="14" r="4" fill="var(--brand-navy)"/>
    </g>

    <g class="icon-handshake" fill="var(--brand-grey)" transform="translate(686 476)">
      <path d="M 0 10 L 12 2 L 20 10 L 8 22 Z"/>
      <path d="M 58 10 L 46 2 L 38 10 L 50 22 Z"/>
      <path d="M 12 14 L 24 6 L 36 8 L 46 18 L 36 38 Q 30 44 22 38 L 10 24 Z"/>
    </g>

    <text class="ring-copy" text-anchor="middle">
      <tspan x="585" y="302">Our Mission at Brightmere Partners is</tspan>
      <tspan x="585" y="318">to provide quality business</tspan>
      <tspan x="585" y="334">services through advice &amp; guidance</tspan>
      <tspan x="585" y="350">together with building long-term</tspan>
      <tspan x="585" y="366">business relationships.</tspan>
    </text>

    <text class="ring-copy" text-anchor="middle">
      <tspan x="446" y="519">To be the leading</tspan>
      <tspan x="446" y="535">accounting firm in our</tspan>
      <tspan x="446" y="551">community, known</tspan>
      <tspan x="446" y="567">for providing business &amp;</tspan>
      <tspan x="446" y="583">individuals with innovatives</tspan>
      <tspan x="446" y="599">&amp; experts support enabling</tspan>
      <tspan x="446" y="615">our clients to achieve</tspan>
      <tspan x="446" y="631">financial success.</tspan>
    </text>

    <text class="ring-copy" text-anchor="middle">
      <tspan x="713" y="545">Integrity and</tspan>
      <tspan x="713" y="561">Professionalism,</tspan>
      <tspan x="713" y="577">Trust and Respect,</tspan>
      <tspan x="713" y="593">Efficiency and</tspan>
      <tspan x="713" y="609">Commitment</tspan>
    </text>
  </svg>
</main>
</body>
</html>
```